New Packaging Design Project

Wine packaging redesign. Retail partner requested a redesign of a private label wine. The old label is attached. Our partner liked the Lantern and Briar label and wanted something similar. There will be a logo added to the top of the label

Went on vacation/holiday

```html
<!DOCTYPE html>
<html lang="en">
<head>
<meta charset="utf-8">
<title>Red Blend Label Series</title>
<link rel="stylesheet" href="https://fonts.googleapis.com/css2?family=Marcellus&family=Open+Sans:wght@300;400&display=swap">
<style>
  :root {
    --backdrop: #160d0e;
    --label-grey: #474747;
    --landscape-dark: #2c2c2c;
    --landscape-mid: #3a342b;
    --gold: #e2ad3c;
    --gold-deep: #8a6a26;
    --white: #f2f2f2;
  }
  html, body {
    margin: 0;
    padding: 0;
    width: 1200px;
    height: 1200px;
    overflow: hidden;
    background: var(--backdrop);
  }
  .label-series {
    position: absolute;
    left: 24px;
    top: 390px;
    display: flex;
    gap: 18px;
  }
  .wine-label {
    position: relative;
    width: 216px;
    height: 420px;
    background: var(--label-grey);
    text-align: center;
    overflow: hidden;
  }
  .region-name {
    margin: 0;
    padding-top: 38px;
    font-family: "Marcellus", serif;
    font-weight: 400;
    font-size: 21px;
    letter-spacing: 0.5px;
    color: var(--gold);
    line-height: 1;
    white-space: nowrap;
  }
  .blend-name {
    margin: 10px 0 0;
    font-family: "Open Sans", sans-serif;
    font-weight: 300;
    font-size: 12px;
    letter-spacing: 0.5px;
    color: var(--gold);
    line-height: 1;
  }
  .varietal {
    margin: 33px 0 0;
    font-family: "Open Sans", sans-serif;
    font-weight: 400;
    font-size: 10px;
    letter-spacing: 0.3px;
    color: var(--white);
    line-height: 1;
    white-space: nowrap;
  }
  .vintage {
    margin: 4px 0 0;
    font-family: "Open Sans", sans-serif;
    font-weight: 400;
    font-size: 7px;
    color: var(--white);
    line-height: 1;
  }
  .vineyard-landscape {
    position: absolute;
    left: 0;
    right: 0;
    top: 137px;
    bottom: 0;
    background: linear-gradient(180deg,
      var(--label-grey) 0%,
      var(--landscape-dark) 14%,
      var(--landscape-mid) 30%,
      var(--gold-deep) 55%,
      var(--landscape-dark) 100%);
  }
</style>
</head>
<body>
  <main class="label-series">
    <article class="wine-label">
      <h1 class="region-name">CEDAR HOLLOW</h1>
      <p class="blend-name">REDBLEND</p>
      <p class="varietal">CABERNET FRANC</p>
      <p class="vintage">2018</p>
      <div class="vineyard-landscape" role="img" aria-label="Illustration of dark hills over gold-lined vineyard rows"></div>
    </article>
    <article class="wine-label">
      <h1 class="region-name">CEDAR HOLLOW</h1>
      <p class="blend-name">REDBLEND</p>
      <p class="varietal">PETIT VERDOT</p>
      <p class="vintage">2018</p>
      <div class="vineyard-landscape" role="img" aria-label="Illustration of dark hills over gold-lined vineyard rows"></div>
    </article>
    <article class="wine-label">
      <h1 class="region-name">CEDAR HOLLOW</h1>
      <p class="blend-name">REDBLEND</p>
      <p class="varietal">CABERNET SAUVIGNON</p>
      <p class="vintage">2018</p>
      <div class="vineyard-landscape" role="img" aria-label="Illustration of dark hills over gold-lined vineyard rows"></div>
    </article>
    <article class="wine-label">
      <h1 class="region-name">CEDAR HOLLOW</h1>
      <p class="blend-name">REDBLEND</p>
      <p class="varietal">MALBEC</p>
      <p class="vintage">2018</p>
      <div class="vineyard-landscape" role="img" aria-label="Illustration of dark hills over gold-lined vineyard rows"></div>
    </article>
    <article class="wine-label">
      <h1 class="region-name">CEDAR HOLLOW</h1>
      <p class="blend-name">REDBLEND</p>
      <p class="varietal">MERLOT</p>
      <p class="vintage">2018</p>
      <div class="vineyard-landscape" role="img" aria-label="Illustration of dark hills over gold-lined vineyard rows"></div>
    </article>
  </main>
</body>
</html>
```